Brivora Collective Business Card Design

We need a business card design for Brivora Collective. We are a healthcare recruiting, wellness and education company. We partner with medical facilities to find quality candidates. We also offer free wellness courses.
The final design should communicate an emphasis on recruiting and wellness
The main purpose of the business card is to utilized it for networking events, give to hospitals, executives, VCs surgery centers and clinics. I want it to be sleek, clean, use of our brand colors and professional.

```html
<!DOCTYPE html>
<html lang="en">
<head>
<meta charset="utf-8">
<title>Brivora Collective – Business Card</title>
<link href="https://fonts.googleapis.com/css2?family=Montserrat:wght@300;400;600;700&display=swap" rel="stylesheet">
<style>
  :root {
    --bg: #b3b3b3;
    --paper: #ffffff;
    --ink: #0b5c55;
    --ink-soft: #2f6f69;
    --teal: #2a9a90;
    --teal-light: #5bb5ac;
    --teal-dark: #1d7f77;
    --white: #ffffff;
  }
  * { box-sizing: border-box; margin: 0; padding: 0; }
  html, body {
    width: 1200px; height: 900px; overflow: hidden;
    background: var(--bg);
    font-family: "Montserrat", sans-serif;
  }
  .stage {
    width: 1200px; height: 900px;
    display: flex; align-items: center; justify-content: center;
    gap: 36px;
  }
  .card {
    width: 550px; height: 314px;
    position: relative;
    box-shadow: 0 8px 22px rgba(0,0,0,0.25);
    overflow: hidden;
    flex: none;
  }
  .card--front { background: var(--paper); border-bottom: 3px solid var(--ink); }

  .brand {
    position: absolute; left: 30px; top: 34px;
    color: var(--ink); line-height: 1;
  }
  .brand__name {
    display: block;
    font-weight: 400; font-size: 50px; letter-spacing: -1.5px;
  }
  .brand__sub {
    display: block; text-align: right;
    font-weight: 400; font-size: 27px; letter-spacing: -0.5px;
    margin-top: 2px;
  }

  .brand-block {
    position: absolute; right: 38px; top: 34px;
    width: 160px; height: 150px;
    border-radius: 16px;
    background: var(--ink);
  }

  .person { position: absolute; left: 30px; top: 132px; color: var(--ink); }
  .person__name { font-weight: 700; font-size: 15px; letter-spacing: 0.2px; }
  .person__title { font-weight: 400; font-size: 12px; color: var(--ink-soft); margin-top: 1px; }

  .contact {
    position: absolute; left: 30px; top: 184px;
    font-size: 12.5px; line-height: 1.45; color: var(--ink-soft);
    list-style: none;
  }
  .contact__address { margin-bottom: 7px; }
  .contact__row { display: flex; align-items: center; gap: 10px; }
  .contact__icon { width: 13px; height: 13px; fill: var(--ink); flex: none; }

  .card--back { background: var(--teal); }
  .back-pattern {
    position: absolute; inset: 0;
    background:
      linear-gradient(115deg, rgba(255,255,255,0.22) 0%, rgba(255,255,255,0.08) 30%, rgba(255,255,255,0) 48%),
      linear-gradient(120deg, var(--teal-light) 0%, var(--teal) 40%, var(--teal-dark) 100%);
  }
  .back-brand {
    position: absolute; left: 300px; top: 50%;
    transform: translateY(-50%);
    display: flex; align-items: center; gap: 10px;
    font-weight: 400; font-size: 20px; color: var(--white);
  }
  .back-brand__square {
    width: 14px; height: 14px; border-radius: 3px; background: var(--white);
  }
</style>
</head>
<body>
<main class="stage">
  <section class="card card--front" aria-label="Card front">
    <p class="brand">
      <span class="brand__name">Brivora</span>
      <span class="brand__sub">Collective</span>
    </p>
    <span class="brand-block" aria-hidden="true"></span>

    <div class="person">
      <p class="person__name">Daniel Ostrander</p>
      <p class="person__title">Principal</p>
    </div>

    <ul class="contact">
      <li class="contact__address">2840 Larkmoor Ave.<br>Aurelia, CO 80412</li>
      <li class="contact__row">
        <svg class="contact__icon" viewBox="0 0 24 24" aria-hidden="true"><path d="M6.6 10.8a15.1 15.1 0 0 0 6.6 6.6l2.2-2.2a1 1 0 0 1 1-.25 11.4 11.4 0 0 0 3.6.57 1 1 0 0 1 1 1V20a1 1 0 0 1-1 1A17 17 0 0 1 3 4a1 1 0 0 1 1-1h3.5a1 1 0 0 1 1 1c0 1.25.2 2.46.57 3.6a1 1 0 0 1-.25 1z"/></svg>
        <span>555 014 2290</span>
      </li>
      <li class="contact__row">
        <svg class="contact__icon" viewBox="0 0 24 24" aria-hidden="true"><path d="M2 5h20v14H2z M2 5l10 8 10-8" fill="none" stroke="#0b5c55" stroke-width="2.4"/></svg>
        <span>info@brivoracollective.com</span>
      </li>
      <li class="contact__row">
        <svg class="contact__icon" viewBox="0 0 24 24" aria-hidden="true"><circle cx="12" cy="12" r="9" fill="none" stroke="#0b5c55" stroke-width="2.4"/><path d="M3 12h18M12 3c3 3 3 15 0 18M12 3c-3 3-3 15 0 18" fill="none" stroke="#0b5c55" stroke-width="1.6"/></svg>
        <span>www.brivoracollective.com</span>
      </li>
    </ul>
  </section>

  <section class="card card--back" aria-label="Card back">
    <div class="back-pattern" role="img" aria-label="Repeating brand motif pattern in light and dark teal tones, lighter toward the upper left"></div>
    <p class="back-brand">
      <span class="back-brand__square" aria-hidden="true"></span>
      <span>Brivora Collective</span>
    </p>
  </section>
</main>
</body>
</html>
```